Design Direct mailer post card for Carpet Cleaning business

We are looking to create a 6.5x 12 eyes cashing direct mail postcard (eddm) for mailed to residential .
This campaign is targeted towards residential customers, with the goal of introducing our service, promote our business, and gain some brand recognition.
The call-to-action is for the prospect to contact us and also schedule a free no obligation demonstration (call, visit our website, or send us an email) to find out information about our service, and to learn more about our service.
4 offers
One Free Room of carpet cleaning
Free bottle spot cleaner
Free Carpet audit
Free chair Cleaning
(See attached picture for offers)
Slogans-You will love your Carpet Again
You want believe the difference
No more Wet Carpet
Dries in minutes not hours
100% natural Safe for Kids and Pets
No harsh chemicals
No sticky residue
Improve air Quailty
100% guaranteed
As far as design, we are looking for a clean and simple layout, not too cluttered, but powerful enough to grab the attention of the reader. Less is more in this case. On the front we were thinking the use of an image & headline and on the back the rest of the information. With that said, please feel free to use your expertise and judgement to conceptualize the best design.
Also attach picture of design and color that I would like.
Target Market(s)
35-70 women middle to upper class
Industry/Entity Type
Cleaning Service

```html
<!DOCTYPE html>
<html lang="en">
<head>
<meta charset="utf-8">
<title>PureNest Carpet Cleaning Postcard</title>
<link href="https://fonts.googleapis.com/css2?family=Roboto:wght@300;400;500;700&family=Roboto+Condensed:wght@400;700&family=Satisfy&display=swap" rel="stylesheet">
<style>
:root{
  --green:#7dc242;
  --cyan:#1fb8d3;
  --orange:#f07f22;
  --ink:#333;
  --soft:#f3f3f3;
  --white:#fff;
  --page:#e4e4e4;
}
*{box-sizing:border-box;margin:0;padding:0}
html,body{width:1102px;height:1200px;overflow:hidden;background:var(--page);font-family:'Roboto',sans-serif;color:var(--ink)}
.card{position:absolute;left:51px;width:1000px;height:542px;background:var(--white);box-shadow:0 4px 14px rgba(0,0,0,.25);overflow:hidden}
.card--front{top:28px}
.card--back{top:620px}
.card-shapes{position:absolute;inset:0;width:100%;height:100%}
.abs{position:absolute}
.brand{position:absolute;left:58px;top:18px}
.brand__name{font-family:'Roboto',sans-serif;font-weight:400;font-size:66px;line-height:1;color:var(--green);letter-spacing:-1px}
.brand__tag{font-weight:300;font-size:21px;color:var(--cyan);margin-left:32px;margin-top:-2px}
.headline{left:26px;top:130px;font-family:'Roboto Condensed',sans-serif;font-weight:700;font-size:27px;color:var(--white);letter-spacing:.3px}
.benefits{left:24px;top:196px;list-style:none;font-size:18px;line-height:25.3px}
.benefits li,.services li{display:flex;align-items:center;gap:7px}
.tick{width:15px;height:15px;flex:none}
.pet-title{left:28px;top:438px;font-family:'Roboto Condensed',sans-serif;font-weight:700;font-size:21px;color:var(--white)}
.pet-copy{left:28px;top:468px;width:370px;font-size:15px;line-height:21px;color:var(--white)}
.dry-badge{left:420px;top:344px;width:160px;height:160px;border-radius:50%;display:flex;flex-direction:column;align-items:center;justify-content:center;text-align:center;color:var(--white);padding:0 16px}
.dry-badge b{font-size:14.5px;line-height:17px;font-weight:700}
.dry-badge span{font-size:13.5px;line-height:16.5px;margin-top:4px}
.contact{text-align:center}
.contact__phone{display:flex;align-items:center;justify-content:center;gap:12px;font-weight:400;font-size:41px;line-height:1}
.contact__web{font-size:16px;margin-top:6px}
.contact--front{left:630px;top:458px;width:330px;color:var(--white)}
.contact--back{left:640px;top:453px;width:330px;color:var(--green)}
.services{left:25px;top:24px;display:grid;grid-template-columns:188px 222px 200px;row-gap:5px;list-style:none;font-size:20px;line-height:25px;color:#444}
.difference{left:28px;top:93px;font-family:'Roboto Condensed',sans-serif;font-weight:700;font-size:27px;color:var(--white)}
.mail-box{border:1px solid #555;font-size:12px;line-height:13px;color:#111}
.mail-box--address{left:670px;top:27px;width:219px;height:76px;padding:8px 15px}
.mail-box--address .route{text-align:center;font-size:10px;margin-bottom:20px}
.mail-box--indicia{left:907px;top:27px;width:76px;height:76px;text-align:center;font-weight:700;font-size:10px;line-height:11.5px;padding-top:8px}
.coupon{top:154px;width:223px;height:118px;background:var(--white);box-shadow:0 2px 4px rgba(0,0,0,.2)}
.coupon__head{background:var(--orange);height:53px;color:var(--white);padding:5px 9px 0;position:relative}
.coupon__free{font-family:'Roboto Condensed',sans-serif;font-weight:700;font-size:27px;line-height:28px}
.coupon__item{position:absolute;right:8px;top:12px;font-family:'Roboto Condensed',sans-serif;font-size:20px;line-height:19px;text-align:right}
.coupon__sub{font-family:'Satisfy',cursive;font-size:12.5px;line-height:14px}
.coupon__body{margin:5px;height:55px;border:1px dashed #b9dd9a;border-top:none;padding:3px 6px;font-size:8.3px;line-height:10.5px;color:#555}
.specials{left:29px;top:300px;width:700px;font-size:19.5px;line-height:28px;color:var(--white)}
.brand--back{left:26px;top:425px}
</style>
</head>
<body>

<section class="card card--front">
  <svg class="card-shapes" viewBox="0 0 1000 542" preserveAspectRatio="none">
    <defs>
      <linearGradient id="photoTone" x1="0" y1="0" x2="1" y2="1">
        <stop offset="0" stop-color="#e9e6e2"/>
        <stop offset=".55" stop-color="#d9c3b2"/>
        <stop offset="1" stop-color="#efeae6"/>
      </linearGradient>
    </defs>
    <rect x="0" y="185" width="620" height="260" fill="var(--soft)"/>
    <g role="img" aria-label="Photo of a smiling young girl lying on a white shag carpet beside a small terrier chewing a bone, with a woman relaxing on a sofa behind">
      <path d="M600 0 H1000 V372 C860 425 720 430 590 412 C545 310 548 150 600 0 Z" fill="url(#photoTone)"/>
    </g>
    <path d="M600 0 C548 150 545 300 590 412" fill="none" stroke="var(--cyan)" stroke-width="12"/>
    <polygon points="0,118 605,118 578,177 0,177" fill="var(--green)"/>
    <path d="M530 402 C700 430 860 425 1000 372 V394 C860 432 700 442 520 414 Z" fill="var(--green)"/>
    <path d="M0 428 C180 392 380 388 520 412 C700 442 860 432 1000 394 V542 H0 Z" fill="var(--cyan)"/>
    <path d="M0 421 C180 385 380 381 520 405" fill="none" stroke="#bfe8f1" stroke-width="5"/>
    <path d="M440 398 L520 406" stroke="var(--green)" stroke-width="4"/>
    <circle cx="383" cy="332" r="36" fill="var(--green)"/>
    <path d="M906 0 H985 V72 L945.5 88 L906 72 Z" fill="var(--orange)"/>
    <circle cx="500" cy="424" r="85" fill="#e9e9e9"/>
    <circle cx="500" cy="424" r="77" fill="var(--orange)"/>
  </svg>

  <div class="brand">
    <div class="brand__name">PureNest</div>
    <div class="brand__tag">Carpet Cleaning &amp; Restoration</div>
  </div>

  <h1 class="abs headline">YOU WILL LOVE YOUR CARPET AGAIN</h1>

  <ul class="abs benefits">
    <li><svg class="tick" viewBox="0 0 16 16"><rect x="1.5" y="3" width="11" height="11" rx="2" fill="none" stroke="var(--green)" stroke-width="1.6"/><path d="M4.5 8 L7.5 11 L14.5 2.5" fill="none" stroke="var(--green)" stroke-width="2"/></svg>No more Wet Carpet</li>
    <li><svg class="tick" viewBox="0 0 16 16"><rect x="1.5" y="3" width="11" height="11" rx="2" fill="none" stroke="var(--green)" stroke-width="1.6"/><path d="M4.5 8 L7.5 11 L14.5 2.5" fill="none" stroke="var(--green)" stroke-width="2"/></svg>Dries in minutes not hours</li>
    <li><svg class="tick" viewBox="0 0 16 16"><rect x="1.5" y="3" width="11" height="11" rx="2" fill="none" stroke="var(--green)" stroke-width="1.6"/><path d="M4.5 8 L7.5 11 L14.5 2.5" fill="none" stroke="var(--green)" stroke-width="2"/></svg>100% natural Safe for Kids and Pets</li>
    <li><svg class="tick" viewBox="0 0 16 16"><rect x="1.5" y="3" width="11" height="11" rx="2" fill="none" stroke="var(--green)" stroke-width="1.6"/><path d="M4.5 8 L7.5 11 L14.5 2.5" fill="none" stroke="var(--green)" stroke-width="2"/></svg>No harsh chemicals</li>
    <li><svg class="tick" viewBox="0 0 16 16"><rect x="1.5" y="3" width="11" height="11" rx="2" fill="none" stroke="var(--green)" stroke-width="1.6"/><path d="M4.5 8 L7.5 11 L14.5 2.5" fill="none" stroke="var(--green)" stroke-width="2"/></svg>No sticky residue</li>
    <li><svg class="tick" viewBox="0 0 16 16"><rect x="1.5" y="3" width="11" height="11" rx="2" fill="none" stroke="var(--green)" stroke-width="1.6"/><path d="M4.5 8 L7.5 11 L14.5 2.5" fill="none" stroke="var(--green)" stroke-width="2"/></svg>Improve air Quailty</li>
    <li><svg class="tick" viewBox="0 0 16 16"><rect x="1.5" y="3" width="11" height="11" rx="2" fill="none" stroke="var(--green)" stroke-width="1.6"/><path d="M4.5 8 L7.5 11 L14.5 2.5" fill="none" stroke="var(--green)" stroke-width="2"/></svg>100% guaranteed</li>
  </ul>

  <h2 class="abs pet-title">Pet Odor &amp; Stain Removal Experts</h2>
  <p class="abs pet-copy">Contact us and also schedule a free no obligation demonstration (call, visit our website, or send us an email) to find out information about our service.</p>

  <div class="abs dry-badge">
    <b>FAST ONE HOUR DRY TIME</b>
    <span>Soft Drying With No Crunchy Residue Safe for Children &amp; Pets</span>
  </div>

  <div class="abs contact contact--front">
    <div class="contact__phone">
      <svg width="34" height="34" viewBox="0 0 34 34"><circle cx="17" cy="17" r="15.5" fill="none" stroke="currentColor" stroke-width="2.5"/><path d="M11 9.5 L14 9 L15.5 13.5 L13.5 15 C14.5 17.5 16.5 19.5 19 20.5 L20.5 18.5 L25 20 L24.5 23 C23.5 24.5 21.5 25 19.5 24 C15 22 12 19 10 14.5 C9.3 12.5 9.8 10.5 11 9.5 Z" fill="currentColor"/></svg>
      555.014.2270
    </div>
    <div class="contact__web">www.purenestcarpetcare.com</div>
  </div>
</section>

<section class="card card--back">
  <svg class="card-shapes" viewBox="0 0 1000 542" preserveAspectRatio="none">
    <path d="M0 133 H1000 V378 C820 410 760 395 600 395 C400 395 200 388 0 425 Z" fill="var(--green)"/>
    <path d="M0 425 C200 388 400 395 600 395 C760 395 820 410 1000 378 V392 C820 424 760 410 600 410 C400 410 200 404 0 440 Z" fill="#d6f0f6"/>
    <path d="M780 372 C860 372 930 360 1000 345 V380 C930 395 860 400 780 398 Z" fill="var(--cyan)"/>
    <polygon points="0,82 628,82 636,90 636,133 0,133" fill="var(--cyan)"/>
    <g role="img" aria-label="Close-up photo of clean beige floor tiles">
      <circle cx="752" cy="382" r="63" fill="#fff"/>
      <circle cx="752" cy="382" r="57" fill="#cfcac4"/>
    </g>
    <g role="img" aria-label="Photo of an upholstery cleaning wand cleaning an olive fabric armchair">
      <circle cx="889" cy="350" r="80" fill="#fff"/>
      <circle cx="889" cy="350" r="74" fill="#7d7b5f"/>
    </g>
  </svg>

  <ul class="abs services">
    <li><svg class="tick" viewBox="0 0 16 16"><rect x="1.5" y="3" width="11" height="11" rx="2" fill="none" stroke="var(--green)" stroke-width="1.6"/><path d="M4.5 8 L7.5 11 L14.5 2.5" fill="none" stroke="var(--green)" stroke-width="2"/></svg>Carpet Cleaning</li>
    <li><svg class="tick" viewBox="0 0 16 16"><rect x="1.5" y="3" width="11" height="11" rx="2" fill="none" stroke="var(--green)" stroke-width="1.6"/><path d="M4.5 8 L7.5 11 L14.5 2.5" fill="none" stroke="var(--green)" stroke-width="2"/></svg>Upholstery Cleaning</li>
    <li><svg class="tick" viewBox="0 0 16 16"><rect x="1.5" y="3" width="11" height="11" rx="2" fill="none" stroke="var(--green)" stroke-width="1.6"/><path d="M4.5 8 L7.5 11 L14.5 2.5" fill="none" stroke="var(--green)" stroke-width="2"/></svg>Odor Removal</li>
    <li><svg class="tick" viewBox="0 0 16 16"><rect x="1.5" y="3" width="11" height="11" rx="2" fill="none" stroke="var(--green)" stroke-width="1.6"/><path d="M4.5 8 L7.5 11 L14.5 2.5" fill="none" stroke="var(--green)" stroke-width="2"/></svg>Tile Cleaning</li>
    <li><svg class="tick" viewBox="0 0 16 16"><rect x="1.5" y="3" width="11" height="11" rx="2" fill="none" stroke="var(--green)" stroke-width="1.6"/><path d="M4.5 8 L7.5 11 L14.5 2.5" fill="none" stroke="var(--green)" stroke-width="2"/></svg>Rug Cleaning</li>
    <li><svg class="tick" viewBox="0 0 16 16"><rect x="1.5" y="3" width="11" height="11" rx="2" fill="none" stroke="var(--green)" stroke-width="1.6"/><path d="M4.5 8 L7.5 11 L14.5 2.5" fill="none" stroke="var(--green)" stroke-width="2"/></svg>Air Duct Cleaning</li>
  </ul>

  <div class="abs mail-box mail-box--address">
    <div class="route">*****************ECRWSS****</div>
    Local<br>Postal Customer
  </div>
  <div class="abs mail-box mail-box--indicia">PRSRT STD<br>ECRWSS<br>U.S. POSTAGE<br>PAID<br>EDDM RETAIL</div>

  <h2 class="abs difference">YOU WANT BELIEVE THE DIFFERENCE!</h2>

  <article class="abs coupon" style="left:28px">
    <div class="coupon__head"><div class="coupon__free">FREE</div><div class="coupon__sub">Save Big!</div><div class="coupon__item">Carpet Audit</div></div>
    <p class="coupon__body">You are under no obligation. A carpet audit is much more than a price quote. We will tell you exactly what we can do to improve your carpet, how good it will look, &amp; how long you can expect it to last.*</p>
  </article>
  <article class="abs coupon" style="left:270px">
    <div class="coupon__head"><div class="coupon__free">FREE</div><div class="coupon__sub">Great Deal!</div><div class="coupon__item">One Room Clean</div></div>
    <p class="coupon__body">Yes, you read that right! We will let you "test drive" our services before you buy! We will clean any room in your home (up to 200 sq. ft), absolutely FREE - no obligation or other purchase necessary!*</p>
  </article>
  <article class="abs coupon" style="left:512px">
    <div class="coupon__head"><div class="coupon__free">FREE</div><div class="coupon__sub">Spot Cleaner for Life!</div><div class="coupon__item">Bottle Of Spot<br>Cleaner</div></div>
    <p class="coupon__body">With any cleaning service we will give a FREE BOTTLE of our trusted home pro spotter with lifetime refills! * (A $89.95 Value)</p>
  </article>
  <article class="abs coupon" style="left:756px">
    <div class="coupon__head"><div class="coupon__free">FREE</div><div class="coupon__sub">Bonus offer!</div><div class="coupon__item">Chair Cleaning</div></div>
    <p class="coupon__body">Normally $59.99, but yours FREE with this offer! Let us clean your sofa or loveseat, and we will clean a chair for FREE.*</p>
  </article>

  <p class="abs specials">Specials only good for use in maple ridge and willow bend. If You Wait You'll Miss out! Call 555.014.2270 right now before the coupons expire or run out!</p>

  <div class="brand brand--back">
    <div class="brand__name">PureNest</div>
    <div class="brand__tag">Carpet Cleaning &amp; Restoration</div>
  </div>

  <div class="abs contact contact--back">
    <div class="contact__phone">
      <svg width="34" height="34" viewBox="0 0 34 34"><circle cx="17" cy="17" r="15.5" fill="none" stroke="currentColor" stroke-width="2.5"/><path d="M11 9.5 L14 9 L15.5 13.5 L13.5 15 C14.5 17.5 16.5 19.5 19 20.5 L20.5 18.5 L25 20 L24.5 23 C23.5 24.5 21.5 25 19.5 24 C15 22 12 19 10 14.5 C9.3 12.5 9.8 10.5 11 9.5 Z" fill="currentColor"/></svg>
      555.014.2270
    </div>
    <div class="contact__web">www.purenestcarpetcare.com</div>
  </div>
</section>

</body>
</html>
```